Music portal needs a sleek mobile app design

We need an innovative, cutting edge design for our mobile app for www.loftaroundsound.com . LOFTAROUND Music is a platform that lets independent musicians upload and share their music for free. Music lovers can discover new music too.

If you visit the website, you'll get an idea of our brand colors and theme. im attaching the logo and our new discover page layout. We use "din Next LT pro" as our brand font.

We are looking for an app optimized for iOS, but can be used on Android and windows too.

Im looking for a design that flows and navigates with user intuition and is sleek, flat style in nature and has Similar apps are tunewharf, riffpantry and beatorchard.

Here are some ideas we like, but please dont copy. Come up with something similar in 'feel'

https://www.portfoliarc.net/gallery/B-TUNE-IT-Music-application/4412983

https://sketchvault.com/shots/2290518-Music-App

The most important pages/ screens for us are:
- The discover screen
- The login and sign up screens
- The splash screen
- The track player screen
- The use profile page screen
Updates

It seems no design has come close to what I was looking for so I will be requesting a refund and withdrawing this project. Thanks for your effort

Target Market(s)

music, music app, tunewharf, loftaround music, music app design

Colors
f78f20
ffcf3e
ffffff
000000

Requirements
Must have
• a sleek easy to use navigation- please create an account on loftaroundsound.com to see how the site works.
Nice to have
• Sleek screen to screen transitions
Should not have
• no 3d designs. Flat design only

```html
<!DOCTYPE html>
<html lang="en">
<head>
<meta charset="utf-8">
<title>Discover Music – Welcome</title>
<link rel="stylesheet" href="https://fonts.googleapis.com/css2?family=Barlow:wght@500;600;700&display=swap">
<style>
  :root {
    --ink: #000000;
    --paper: #ffffff;
    --orange: #f78f20;
    --grey-btn: #b9b9b9;
    --photo-dark: #141016;
    --photo-mid: #2a2328;
    --photo-warm: #3a2c2a;
  }
  * { margin: 0; padding: 0; box-sizing: border-box; }
  html, body { width: 677px; height: 1200px; overflow: hidden; background: var(--ink); }
  body { font-family: "Barlow", "Helvetica Neue", Arial, sans-serif; color: var(--paper); }

  .screen { position: relative; width: 677px; height: 1200px; overflow: hidden; }

  .backdrop {
    position: absolute; inset: 0;
    background:
      radial-gradient(ellipse 420px 520px at 150px 640px, #4a4446 0%, #262022 55%, transparent 80%),
      radial-gradient(ellipse 300px 500px at 560px 700px, #3b3433 0%, transparent 75%),
      linear-gradient(180deg, var(--photo-warm) 0%, var(--photo-mid) 45%, var(--photo-dark) 100%);
  }
  .backdrop-shade {
    position: absolute; inset: 0;
    background: linear-gradient(180deg, rgba(0,0,0,0.15) 0%, rgba(0,0,0,0.35) 60%, rgba(0,0,0,0.75) 100%);
  }

  .intro { position: absolute; left: 0; right: 0; top: 376px; text-align: center; }
  .intro-icon { width: 116px; height: 116px; display: block; margin: 0 auto; }
  .intro-title { margin-top: 24px; font-size: 30px; font-weight: 700; letter-spacing: 0.3px; }

  .pager { position: absolute; top: 952px; left: 0; right: 0; display: flex; justify-content: center; gap: 22px; }
  .pager-dot { width: 17px; height: 17px; border-radius: 50%; border: 2px solid var(--paper); }
  .pager-dot.is-active { background: var(--paper); }

  .actions { position: absolute; top: 1016px; left: 32px; right: 32px; display: flex; gap: 18px; }
  .btn {
    flex: 1; height: 64px; border-radius: 32px;
    display: flex; align-items: center; justify-content: center;
    font-size: 28px; font-weight: 700; color: var(--paper);
  }
  .btn-join { background: var(--grey-btn); }
  .btn-signin { background: var(--orange); }

  .discover-link { position: absolute; top: 1121px; left: 0; right: 0; text-align: center; font-size: 27px; font-weight: 600; }
</style>
</head>
<body>
  <main class="screen">
    <div class="backdrop" role="img" aria-label="Photo of a DJ's hand on a turntable record beside a mixer, in dark tones"></div>
    <div class="backdrop-shade"></div>

    <section class="intro">
      <svg class="intro-icon" viewBox="0 0 116 116" aria-hidden="true">
        <g fill="none" stroke="#ffffff" stroke-width="6" stroke-linejoin="round">
          <path d="M36 86 V28 L96 16 V74"/>
          <path d="M36 40 L96 28"/>
          <ellipse cx="25" cy="88" rx="12" ry="10"/>
          <ellipse cx="85" cy="76" rx="12" ry="10"/>
        </g>
      </svg>
      <h1 class="intro-title">Discover music that will inspire you.</h1>
    </section>

    <nav class="pager" aria-label="Intro pages">
      <span class="pager-dot"></span>
      <span class="pager-dot is-active"></span>
      <span class="pager-dot"></span>
    </nav>

    <div class="actions">
      <div class="btn btn-join">Join now</div>
      <div class="btn btn-signin">Sign In</div>
    </div>

    <p class="discover-link">Discover Music</p>
  </main>
</body>
</html>
```